Marketing One-Sheet for Security Deposit Claim Notice

I need a one-sheet flyer formatted for email distribution — optimized as a JPEG/PNG that I can insert into Constant Contact or Outlook. I do not want to attach it to an email, but insert it in the email we send out. I would like it to look professional but engaging. Some images would be good, but want to make sure it reads well if images do not load for the recipients. The text is in the attached Word document, but I am open to changes/ideas that may be better for marketing purposes. I included the URLs for some of the links I would like in the one-sheet that is clickable. The logo for the business is being uploaded on the Word document. Proposed text is also uploaded in a Word document. Thank you.

Target Market(s)

Landlords, Real Estate Agents, Property Managers

Industry/Entity Type

Legal

Requirements
Must have
• Professional but appealing design. The One-sheet is going to be placed in the body of emails, not as an attachment.
Nice to have
• Include our logo for the business and the web links please.
Should not have
• Images can be ok, but it needs to look right if images do not download from the email sent out.

```html
<!DOCTYPE html>
<html lang="en">
<head>
<meta charset="utf-8">
<title>Security Deposit Claim Notice – Tenancy Legal Group</title>
<link href="https://fonts.googleapis.com/css2?family=Cinzel:wght@700;900&family=Red+Hat+Display:ital,wght@0,400;0,500;0,700;0,800;1,500&display=swap" rel="stylesheet">
<style>
  :root{
    --crimson:#b71f2e;
    --ink:#111111;
    --text:#2b2b2b;
    --cream:#f7f4d3;
    --fee-cream:#f9f3c4;
    --white:#ffffff;
    --stage:#e9e7e3;
    --rule:#dcdcdc;
  }
  *{box-sizing:border-box;margin:0;padding:0}
  html,body{width:1200px;height:1117px;overflow:hidden}
  body{background:var(--stage);font-family:"Red Hat Display",sans-serif;color:var(--text)}
  .sheet{position:absolute;left:210px;top:8px;width:780px;height:1100px;background:var(--white);overflow:hidden;box-shadow:0 2px 10px rgba(0,0,0,.12)}
  .abs{position:absolute}

  /* header */
  .brand{left:40px;top:62px;width:250px}
  .brand-name{display:flex;align-items:center;gap:10px;font-family:"Red Hat Display",sans-serif;font-weight:800;color:var(--crimson);font-size:24px;line-height:1.1;white-space:nowrap}
  .brand-mark{width:18px;height:18px;background:var(--crimson);flex:none}
  .brand-web,.brand-phone{font-weight:800;color:var(--crimson);font-size:16px;line-height:1.35}
  .brand-web{margin-top:14px}
  .hero-photo{left:302px;top:0;width:478px;height:213px;background:linear-gradient(135deg,#d9d9d9 0%,#9a9a9a 45%,#4b4b4b 100%)}

  /* title band */
  .title-band{left:0;top:213px;width:780px;height:145px;background:var(--crimson)}
  .title{left:0;top:226px;width:780px;text-align:center;font-family:"Cinzel",serif;font-weight:700;font-size:37px;color:var(--white);letter-spacing:.5px}
  .title .accent{color:var(--fee-cream)}
  .subtitle{left:0;top:274px;width:780px;text-align:center;font-style:italic;font-weight:500;color:var(--white);font-size:20px}

  /* benefits bar */
  .benefits{left:54px;top:313px;width:672px;height:93px;background:var(--ink);border-radius:12px;display:flex;align-items:center;padding:0 28px}
  .benefit{display:flex;align-items:center;gap:14px;color:var(--white);font-weight:700;font-size:15.5px;line-height:1.15;height:64px;white-space:nowrap}
  .benefit + .benefit{border-left:2px solid var(--crimson);padding-left:16px;margin-left:14px}
  .benefit-icon{width:62px;height:62px;border-radius:50%;background:var(--crimson);border:3px solid var(--white);display:flex;align-items:center;justify-content:center;flex:none}
  .benefit:nth-child(1){width:190px}
  .benefit:nth-child(2){width:210px}

  /* services */
  .service-heading{left:30px;top:447px;width:330px;text-align:center;font-family:"Cinzel",serif;font-weight:900;font-size:37.5px;line-height:1.03;color:var(--ink)}
  .fee-box{left:54px;top:623px;width:318px;height:196px;background:var(--crimson);border-radius:14px;text-align:center;color:var(--white);font-family:"Cinzel",serif;font-weight:900}
  .fee-label{font-size:50px;line-height:1;margin-top:18px}
  .fee-amount{font-size:112px;line-height:1;color:var(--fee-cream);letter-spacing:-3px;margin-top:-2px}

  .law-tab{left:416px;top:430px;width:364px;height:61px;background:var(--crimson);color:var(--white);font-weight:800;font-size:19px;line-height:1.06;padding:10px 0 0 15px}
  .law-points{left:416px;top:506px;width:330px;list-style:none}
  .law-points li{position:relative;padding-left:22px;font-size:15px;line-height:1.25;margin-bottom:18px;color:var(--text)}
  .law-points li svg{position:absolute;left:0;top:4px}
  .law-points li:nth-child(1){margin-bottom:23px}
  .risk-note{left:394px;top:651px;width:337px;height:168px;border:1px solid var(--rule);border-radius:14px;padding:14px 18px;font-size:15px;line-height:1.27;color:var(--text)}

  .commercial{left:0;top:863px;width:780px;text-align:center;color:var(--crimson);font-weight:800;font-size:21.5px;letter-spacing:-.2px}

  /* footer */
  .footer{left:0;top:929px;width:780px;height:171px;background:var(--cream)}
  .cta{left:77px;top:911px;width:626px;height:35px;background:var(--ink);border-radius:18px;color:var(--white);font-weight:700;font-size:18px;text-align:center;line-height:35px}
  .contact{left:0;top:961px;width:780px;display:flex;justify-content:center;align-items:center;gap:12px;font-weight:700;font-size:20px;color:var(--ink)}
  .contact .sep{width:2px;height:20px;background:var(--crimson)}
  .contact span{display:flex;align-items:center;gap:6px}
  .link-box{top:1022px;height:37px;border:1.5px solid var(--ink);border-radius:5px;font-size:13.5px;font-weight:500;color:var(--ink);text-decoration:none;display:flex;align-items:center;justify-content:center}
  .link-box .legend{position:absolute;top:-9px;left:50%;transform:translateX(-50%);background:var(--cream);padding:0 8px;color:var(--crimson);font-weight:700;font-size:11.5px;white-space:nowrap}
  .link-more{left:49px;width:376px}
  .link-hire{left:448px;width:283px}
</style>
</head>
<body>
<main class="sheet">
  <header>
    <div class="abs brand">
      <div class="brand-name"><span>Tenancy Legal Group</span><span class="brand-mark"></span></div>
      <p class="brand-web">TenancyLegalGroup.com</p>
      <p class="brand-phone">1(800) 555-0142</p>
    </div>
    <div class="abs hero-photo" role="img" aria-label="Photo of two people at a desk reviewing and signing a rental contract beside a laptop"></div>
  </header>

  <div class="abs title-band"></div>
  <h1 class="abs title">Security Deposit <span class="accent">Claim Notice</span></h1>
  <p class="abs subtitle">Keep the tenant’s Security Deposit</p>

  <section class="abs benefits">
    <div class="benefit">
      <div class="benefit-icon">
        <svg width="32" height="32" viewBox="0 0 32 32" fill="none" stroke="#fff" stroke-width="2.4"><circle cx="10" cy="10" r="6"/><path d="M14 14l12 12M21 21l3-3M24 24l2-2"/></svg>
      </div>
      <span>Cover unpaid<br>Rent</span>
    </div>
    <div class="benefit">
      <div class="benefit-icon">
        <svg width="32" height="32" viewBox="0 0 32 32" fill="#fff"><path d="M16 4L3 15h4v13h18V15h4z"/><rect x="13" y="19" width="6" height="9" fill="#b71f2e"/></svg>
      </div>
      <span>Charge against<br>Damages to the<br>Property</span>
    </div>
    <div class="benefit">
      <div class="benefit-icon">
        <svg width="30" height="32" viewBox="0 0 30 32" fill="none" stroke="#fff" stroke-width="2.2"><rect x="4" y="3" width="20" height="26" rx="2"/><path d="M9 10h10M9 15h10M9 20h6"/><circle cx="22" cy="24" r="4" fill="#fff"/></svg>
      </div>
      <span>Apply to legal<br>fees and costs</span>
    </div>
  </section>

  <h2 class="abs service-heading">We Prepare Security Deposit Claim Notices</h2>
  <div class="abs fee-box">
    <p class="fee-label">FLAT FEE</p>
    <p class="fee-amount">$350</p>
  </div>

  <h3 class="abs law-tab">FOLLOW FLORIDA LAW TO<br>KEEP THE DEPOSIT</h3>
  <ul class="abs law-points">
    <li><svg width="12" height="12" viewBox="0 0 12 12"><circle cx="6" cy="6" r="6" fill="#b71f2e"/><path d="M3.2 6.2l2 1.8 3.5-3.6" stroke="#fff" stroke-width="1.6" fill="none"/></svg>Tenant is automatically entitled to<br>their full deposit back</li>
    <li><svg width="12" height="12" viewBox="0 0 12 12"><circle cx="6" cy="6" r="6" fill="#b71f2e"/><path d="M3.2 6.2l2 1.8 3.5-3.6" stroke="#fff" stroke-width="1.6" fill="none"/></svg>No claim against the deposit can be made</li>
    <li><svg width="12" height="12" viewBox="0 0 12 12"><circle cx="6" cy="6" r="6" fill="#b71f2e"/><path d="M3.2 6.2l2 1.8 3.5-3.6" stroke="#fff" stroke-width="1.6" fill="none"/></svg>Tenant can sue and recover the deposit<br>and thousands in legal fees</li>
  </ul>
  <p class="abs risk-note">There are lawyers that specialize in representing tenants and go after landlords that do not make a proper claim against the security deposit. They sue and win their cases and get thousands of dollars in legal fees against Landlords, even if the tenant owes unpaid rent.</p>

  <p class="abs commercial">FOR COMMERCIAL PROPERTIES, THE FLAT LEGAL FEE IS $450.</p>

  <footer>
    <div class="abs footer"></div>
    <p class="abs cta">Hire Us to prepare and serve to the tenant the security deposit claim</p>
    <div class="abs contact">
      <span>Tenancy Legal Group</span>
      <i class="sep"></i>
      <span><svg width="18" height="18" viewBox="0 0 18 18"><circle cx="9" cy="9" r="9" fill="#b71f2e"/><circle cx="9" cy="9" r="5.5" fill="none" stroke="#fff" stroke-width="1.2"/><path d="M3.5 9h11M9 3.5c-3 3.5-3 7.5 0 11M9 3.5c3 3.5 3 7.5 0 11" stroke="#fff" stroke-width="1.1" fill="none"/></svg>TenancyLegalGroup.com</span>
      <i class="sep"></i>
      <span><svg width="16" height="18" viewBox="0 0 16 18"><path d="M3 1l3 .5 1.5 4-2 1.5c1 2.5 2.5 4 5 5.5l1.5-2 4 1.5.5 3c-1 2-3 2.5-5 1.5C6 14.5 2.5 10.5 1 6 .5 3.5 1 2 3 1z" fill="#b71f2e"/></svg>1800-555-0142</span>
    </div>
    <a class="abs link-box link-more" href="https://tenancylegalgroup.com/deposit-claims/"><span class="legend">MORE INFORMATION</span>https://tenancylegalgroup.com/deposit-claims/</a>
    <a class="abs link-box link-hire" href="https://tenancylegalgroup.com/retain-us/"><span class="legend">REQUEST OUR HIRING DOCUMENTS</span>https://tenancylegalgroup.com/retain-us/</a>
  </footer>
</main>
</body>
</html>
```